Equine Horse Employment site

We need to redesign the layout of Paddock Crew.co.uk

It will offer Job seekers and Employers the place to look for a job, and look for a candidate.

The logical format needs to be improved and the layout must look highly visually appealing.

It needs to be incredibly simple to use and one click access to any part of the site.

The homepage must convey the following

- Log in and register areas
- Current Job Listings
- Current CV's
- Exclusive Service Club button
- Search box to allow simple searching for Jobs or CVs

We need PSD layouts for Homepage, Job listing Page, CV listing Page, Job Profile and CV Profile. This job is for the design of 5 PSD screens.

Generic page for ancillary page such as about, contact and news.

The biggest competitor is StableandTack.com

Please ask us any questions and please be prepared to make changes, as we are very particular.

More work will be provided to the winning designer.

thanks

• It must not look cheap or like a job board, it has to have character and feel friendly, and inviting. Please do not submit poor designs that look like a job board, as they will be rejected instantly.

thanks

```html
<!DOCTYPE html>
<html lang="en">
<head>
<meta charset="utf-8">
<title>Paddock Crew — Equestrian Recruitment</title>
<link rel="stylesheet" href="https://fonts.googleapis.com/css2?family=Ubuntu:wght@300;400;500;700&family=Open+Sans:wght@400;600&family=Oswald:wght@400&display=swap">
<style>
:root{
  --green:#3f7a22;
  --green-dark:#2f5f18;
  --green-head:#356d1b;
  --lime:#9dc13b;
  --lime-dark:#7e9f26;
  --text:#4a4a4a;
  --row-alt:#ececec;
  --bar:#ececec;
  --line:#d6d6d6;
  --brown:#8a5416;
  --brown-dark:#6e3f0c;
  --dark:#454545;
  --white:#fff;
  --brand-red:#a3262a;
}
*{box-sizing:border-box;margin:0;padding:0}
html,body{width:960px;height:1200px;overflow:hidden;background:var(--white)}
body{position:relative;font-family:"Ubuntu",sans-serif;color:var(--text)}
.abs{position:absolute}
a{color:inherit;text-decoration:none}

/* top bar */
.topbar{left:0;top:0;width:960px;height:44px;background:var(--bar);border-bottom:1px solid var(--line)}
.call{left:40px;top:15px;font-size:13px;color:#444;white-space:nowrap}
.call strong{font-size:16px;color:var(--green-dark);margin-left:5px;font-weight:500;position:relative;top:1px}
.top-divider{left:204px;top:8px;width:1px;height:30px;background:#555}
.social{top:12px;width:24px;height:24px;border-radius:50%;background:#d2d2d2;border:1px solid #c4c4c4}
.main-nav{right:139px;top:16px;font-size:13px;color:#444;white-space:nowrap}
.main-nav a{padding:0 6px}
.main-nav a:last-child{padding-right:0}
.main-nav a.current{color:var(--green-dark)}
.main-nav span{color:#777}
.employers{left:840px;top:7px;width:79px;height:30px;background:#4a4a4a;color:#fff;font-size:13px;font-weight:500;text-align:center;line-height:28px;border-radius:2px;border:1px solid #333}

/* brand */
.brand{left:38px;top:88px;display:flex;align-items:center;gap:8px}
.brand-mark{width:20px;height:20px;background:var(--brand-red)}
.brand-name{font-size:21px;color:#222;font-weight:400;letter-spacing:.5px;line-height:24px}
.brand-tag{left:66px;top:115px;font-size:7.5px;color:var(--brand-red)}
.club{left:642px;top:80px;width:276px;height:44px;border-radius:3px;border:1px solid var(--lime-dark);background:linear-gradient(#b4d454,#96bb34);display:flex;align-items:center}
.club-icon{width:40px;height:40px;border-radius:50%;background:#3c3c3c;margin-left:2px;border:2px solid #6d6d6d}
.club-text{font-size:16px;color:var(--green-dark);margin-left:7px;white-space:nowrap}

/* welcome */
.welcome{left:26px;top:157px;width:614px;height:298px;border:1px solid var(--line);background:linear-gradient(#ececec,#fafafa 40%,#fff)}
.welcome h1{position:absolute;left:0;right:0;top:32px;text-align:center;font-size:32px;font-weight:500;color:var(--green-dark)}
.welcome p{position:absolute;left:16px;right:16px;top:74px;text-align:center;font-size:18.5px;line-height:23px;color:#555;font-weight:300}
.search{left:10px;top:135px;width:596px;height:141px;background:linear-gradient(var(--green-head),#4b8a28);border:1px solid #2e5b16}
.search h2{position:absolute;left:16px;top:20px;font-size:22px;color:#fff;font-weight:400}
.field{position:absolute;top:56px;height:25px;background:#eee;border:1px solid #d0d0d0;font-size:12.5px;color:#444;padding-left:9px;line-height:23px}
.arrows{position:absolute;right:5px;top:3px}
.view-all{position:absolute;left:18px;top:102px;font-size:12.5px;color:#fff;font-weight:500}
.btn-lime{background:linear-gradient(#b9d85b,#94b733);border:1px solid #6f8d1e;color:var(--green-dark);font-weight:500;text-align:center;border-radius:2px;white-space:nowrap}
.search .btn-lime{position:absolute;left:492px;top:97px;width:82px;height:27px;font-size:16px;line-height:25px}

/* panels */
.panel{border:1px solid var(--line);background:#fff}
.panel-head{height:34px;background:linear-gradient(var(--green-head),#4b8a28);color:#fff;font-size:19px;font-weight:500;padding-left:15px;line-height:34px}
.row{position:relative;padding:0 12px}
.row.alt{background:var(--row-alt)}
.row h3{position:absolute;left:12px;font-size:14.5px;font-weight:500;color:var(--green-dark);white-space:nowrap}
.row h3 small{font-size:12px;text-transform:uppercase;font-weight:500;margin-left:3px}
.row p{position:absolute;left:12px;font-family:"Open Sans",sans-serif;font-size:11.5px;color:#555;line-height:12px}
.meta{position:absolute;right:10px;font-size:12.5px;color:#444;white-space:nowrap}
.meta span{color:#888;margin:0 6px}
.more{position:absolute;height:27px;font-size:13px;line-height:25px}

/* login */
.login{left:654px;top:156px;width:280px;height:247px}
.login .panel-head{height:42px;line-height:40px;font-size:18px;padding-left:18px}
.login label{position:absolute;left:14px;font-size:13.5px;color:#444}
.login .input{position:absolute;left:92px;width:179px;height:27px;background:#f1f1f1;border:1px solid #d0d0d0;border-radius:2px}
.forgot{position:absolute;right:14px;top:140px;font-size:11.5px;color:#444}
.login-btn{position:absolute;left:112px;top:160px;width:86px;height:32px;background:linear-gradient(#4b8a28,var(--green-dark));border:1px solid #24500f;color:#fff;font-size:15px;text-align:center;line-height:30px;border-radius:2px}
.register{position:absolute;left:0;right:0;top:218px;text-align:center;font-size:13px;color:#444}
.register b{color:var(--green-dark);font-weight:700}

/* promo */
.promo{left:654px;top:420px;width:278px;height:139px;background:linear-gradient(var(--brown-dark),var(--brown) 60%,#9a6522);color:#fff;text-align:center;border:1px solid #5e3509}
.promo .big{font-family:"Oswald",sans-serif;font-size:20px;line-height:24px;text-transform:uppercase}
.promo .small{font-size:12.5px;margin-top:6px}
.promo .sponsor{position:absolute;right:8px;bottom:6px;font-size:13px}

.partners-title{left:660px;top:578px;font-size:18px;font-weight:500;color:var(--green-dark)}
.badge{background:#e6e6e6;border:1px solid #b5b5b5}
.badge.dark{background:#555;border-color:#333}

/* newsletter */
.newsletter{left:656px;top:823px;width:279px;height:149px;background:var(--dark);border:1px solid #333}
.newsletter h2{height:42px;line-height:44px;padding-left:13px;font-size:18.5px;font-weight:500;color:#fff;border-bottom:1px solid #5c5c5c}
.newsletter .input{position:absolute;left:10px;top:64px;width:241px;height:24px;background:#eee;border:1px solid #ccc;font-size:12.5px;color:#777;padding-left:8px;line-height:22px}
.newsletter .btn-lime{position:absolute;left:168px;top:100px;width:83px;height:33px;font-size:14px;line-height:31px;font-weight:700}

.about h2{font-size:17px;font-weight:500;color:#444}
.about p{margin-top:9px;font-family:"Open Sans",sans-serif;font-size:11.3px;line-height:17.5px;color:#555;text-align:justify;width:274px}

/* footer */
.footer{left:0;top:1147px;width:960px;height:53px;background:var(--dark)}
.footer nav{position:absolute;left:40px;top:13px;font-size:12.5px;color:#fff;white-space:nowrap}
.footer nav a{padding:0 7px}
.footer nav a:first-child{padding-left:0}
.footer .copy{position:absolute;right:24px;bottom:4px;font-size:9.5px;color:#ddd}
</style>
</head>
<body>

<header class="abs topbar">
  <div class="abs call">CALL US <strong>555 014 2290</strong></div>
  <div class="abs top-divider"></div>
  <span class="abs social" style="left:220px" aria-label="Social profile"></span>
  <span class="abs social" style="left:254px" aria-label="Social profile"></span>
  <nav class="abs main-nav">
    <a class="current">Home</a><span>|</span><a>About us</a><span>|</span><a>News</a><span>|</span><a>Advertise</a><span>|</span><a>Resources</a>
  </nav>
  <a class="abs employers">Employers</a>
</header>

<div class="abs brand"><span class="brand-mark"></span><span class="brand-name">Paddock Crew</span></div>
<div class="abs brand-tag">Equestrian Recruitment Specialists</div>

<a class="abs club"><span class="club-icon"></span><span class="club-text">Join our exclusive service club</span></a>

<section class="abs welcome">
  <h1>Welcome to Paddock Crew</h1>
  <p>your online resource for all Jobs within the Equestrian Industry. A simple, quick and efficient online tool to find a job and fill a position.</p>
  <div class="abs search">
    <h2>Search jobs</h2>
    <div class="field" style="left:17px;width:185px">Enter keyword</div>
    <div class="field" style="left:218px;width:185px">Job type
      <svg class="arrows" width="10" height="18" viewBox="0 0 10 18"><path d="M5 0L10 7H0Z M5 18L0 11H10Z" fill="#999"/></svg></div>
    <div class="field" style="left:415px;width:170px">Job location
      <svg class="arrows" width="10" height="18" viewBox="0 0 10 18"><path d="M5 0L10 7H0Z M5 18L0 11H10Z" fill="#999"/></svg></div>
    <a class="view-all">View all jobs</a>
    <a class="btn-lime">Search</a>
  </div>
</section>

<section class="abs panel" style="left:26px;top:472px;width:614px;height:299px">
  <div class="panel-head">Current job listing</div>
  <div class="row" style="height:61px">
    <h3 style="top:14px;left:14px">Groom</h3>
    <p style="top:36px;left:14px">Usual yard duties</p>
    <div class="meta" style="top:44px">Location<span>|</span>Posted 12. Jun, 2012</div>
  </div>
  <div class="row alt" style="height:70px">
    <h3 style="top:12px">Yard Person</h3>
    <p style="top:35px">To work on a busy yard, mucking out, sweeping leading horsess. Bedding ...</p>
    <div class="meta" style="top:50px;right:13px">Location<span>|</span>Posted 12. Jun, 2012</div>
  </div>
  <div class="row" style="height:130px">
    <h3 style="top:12px">Polo Groom</h3>
    <p style="top:35px">Looking after our clients polo ponies to a very high standard. Horses ...</p>
    <div class="meta" style="top:52px;right:13px">Location<span>|</span>Posted 12. Jun, 2012</div>
    <a class="more btn-lime" style="left:504px;top:90px;width:97px">View more jobs</a>
  </div>
</section>

<section class="abs panel" style="left:26px;top:790px;width:614px;height:345px">
  <div class="panel-head">Current CV</div>
  <div class="row" style="height:89px">
    <h3 style="top:16px;left:15px">Maya 21 <small>Student from California</small></h3>
    <p style="top:38px;left:15px;width:380px;text-align:justify">I've been riding since I was 7 and am now 21. I took lessons in dressage and hunter jumper, and showed locally for several years; I've also taught others to ride and jump in private lessons.</p>
    <div class="meta" style="top:67px">Appln 1023<span>|</span>Posted 12. Jun, 2012</div>
  </div>
  <div class="row alt" style="height:89px">
    <h3 style="top:14px;left:15px">Maya 21 <small>Student from California</small></h3>
    <p style="top:37px;left:15px;width:380px;text-align:justify">I've been riding since I was 7 and am now 21. I took lessons in dressage and hunter jumper, and showed locally for several years; I've also taught others to ride and jump in private lessons.</p>
    <div class="meta" style="top:66px">Appln 1023<span>|</span>Posted 12. Jun, 2012</div>
  </div>
  <div class="row" style="height:131px">
    <h3 style="top:13px">Maya 21 <small>Student from California</small></h3>
    <p style="top:35px;width:380px;text-align:justify">I've been riding since I was 7 and am now 21. I took lessons in dressage and hunter jumper, and showed locally for several years; I've also taught others to ride and jump in private lessons.</p>
    <div class="meta" style="top:63px;right:13px">Appln 1023<span>|</span>Posted 12. Jun, 2012</div>
    <a class="more btn-lime" style="left:500px;top:89px;width:97px">View more CV</a>
  </div>
</section>

<aside class="abs panel login">
  <div class="panel-head">Candidate Login</div>
  <label style="top:73px">Username</label>
  <div class="input" style="top:68px"></div>
  <label style="top:118px">Password</label>
  <div class="input" style="top:111px;left:93px"></div>
  <a class="forgot">Forgot Password</a>
  <a class="login-btn">Login</a>
  <div class="register">New user. To Register <b>Click here</b></div>
</aside>

<aside class="abs promo">
  <div class="big" style="margin-top:10px">Unbeatable job posting<br>from just $30</div>
  <div class="small">Now with over 1.9 million jobs view &nbsp;a week</div>
  <div class="big" style="margin-top:2px">You are in right place</div>
  <div class="sponsor">Sponsored by Saddle &amp; Spur</div>
</aside>

<h2 class="abs partners-title">Who we work with</h2>
<div class="abs badge" style="left:665px;top:616px;width:57px;height:62px" aria-label="Partner badge"></div>
<div class="abs badge" style="left:766px;top:621px;width:55px;height:56px" aria-label="Partner badge"></div>
<div class="abs badge dark" style="left:859px;top:619px;width:73px;height:55px" aria-label="Partner badge"></div>
<div class="abs badge" style="left:729px;top:708px;width:170px;height:32px" aria-label="Partner badge"></div>
<div class="abs badge" style="left:664px;top:756px;width:265px;height:48px;background:#9e9e9e" aria-label="Partner badge"></div>

<aside class="abs newsletter">
  <h2>Subscribe to Newsletter</h2>
  <div class="input">Enter email id</div>
  <a class="btn-lime">SUBMIT</a>
</aside>

<aside class="abs about" style="left:655px;top:993px">
  <h2>About</h2>
  <p>Equestrian Jobs at PaddockCrew. A precise way for equine job seekers and employers to conduct a search for qualified candidates and jobs. No1 in Seekly and a reach of over 500,000 users in the UK alone. Now partnered with Tackboard providing greater reach to the best talent in Europe.</p>
</aside>

<footer class="abs footer">
  <nav>
    <a>Home</a>|<a>About us</a>|<a>Equine Job Seekers</a>|<a>Equine Employers</a>|<a>News</a>|<a>Advertise</a>|<a>Resources</a>|<a>Login</a>|<a>Sitemap</a>
  </nav>
  <div class="copy">Copyright 2012 Paddock Crew. All rights reserved.</div>
</footer>

</body>
</html>
```